To design a brand identity that is simple and creative with 'Valdor' as the brand name, I like modern simple fonts like helvetica neue, I want to print both sides of the card, I am open to dark front and white back, but the design needs to transfer well to letter heads and email signatures, I am looking for sophisticated and elegant, but open minded about clever and off the wall, I do not do 'boring' Valdor Holdings is the mother company for a small group, specialising in Management & consulting, Software development and construction, we have a high level of integrity, we are transparent and accountable for what we do. my images are provided as a guide only, Im not expecting them to be just copied, Im looking for a creator and passionate thinker, who will put life into their work.

Target Market(s)

usually business minded people who are looking for something different in me, such as leadership, confidence and focus with thinking that is per haps a little outside the box..

Industry/Entity Type

Construction

Requirements
Must have
• clean, minmalistic
Nice to have
• custom logo
Should not have
• boring, traditional

```html
<!DOCTYPE html>
<html lang="en">
<head>
<meta charset="utf-8">
<title>Valdor — Business Card</title>
<link rel="stylesheet" href="https://fonts.googleapis.com/css2?family=Quicksand:wght@400&family=Roboto:wght@300;700&family=Lora:ital@1&display=swap">
<style>
  :root {
    --stage: #ece9e4;
    --paper: #fbfbfb;
    --paper-shade: #eeeeee;
    --ink-dark: #2a2a2a;
    --ink-dark-edge: #3a3a3a;
    --brand-orange: #e0663a;
    --brand-red: #e24a3e;
    --soft-orange: #ee8b6a;
    --tagline-grey: #b9b4ae;
    --mark-amber: #e3a51c;
    --band-warm: #d98a2e;
    --band-deep: #9a3a44;
  }
  * { box-sizing: border-box; margin: 0; padding: 0; }
  html, body { width: 1200px; height: 762px; overflow: hidden; }
  body {
    background: var(--stage);
    position: relative;
  }
  .card {
    position: absolute;
    top: 222px;
    width: 520px;
    height: 318px;
    box-shadow: 0 10px 28px rgba(0,0,0,0.18);
  }

  /* Back side */
  .card--back {
    left: 50px;
    background: linear-gradient(135deg, var(--paper) 0%, var(--paper-shade) 100%);
    font-family: "Roboto", sans-serif;
  }
  .back-brand {
    position: absolute;
    top: 30px;
    left: 0;
    width: 100%;
    display: flex;
    justify-content: center;
    align-items: center;
    gap: 10px;
  }
  .back-brand__mark {
    width: 26px; height: 26px; border-radius: 50%;
    background: var(--mark-amber);
  }
  .back-brand__text { display: flex; flex-direction: column; }
  .back-brand__name {
    font-family: "Quicksand", sans-serif;
    font-size: 26px;
    line-height: 1;
    color: var(--brand-orange);
  }
  .back-brand__tagline {
    font-family: "Lora", serif;
    font-style: italic;
    font-size: 6px;
    color: var(--tagline-grey);
    text-align: right;
    margin-top: 2px;
  }
  .contact {
    position: absolute;
    top: 108px;
    left: 42px;
  }
  .contact__email {
    font-weight: 700;
    font-size: 22px;
    color: var(--brand-red);
    letter-spacing: 0.2px;
  }
  .contact__role,
  .contact__line {
    font-weight: 300;
    color: var(--soft-orange);
  }
  .contact__role { font-size: 17px; margin-top: 2px; }
  .contact__line { font-size: 15px; margin-top: 10px; }
  .contact__line + .contact__line { margin-top: 4px; }
  .back-rule {
    position: absolute;
    left: 30px;
    right: 30px;
    top: 250px;
    height: 1.5px;
    background: var(--brand-orange);
  }
  .services {
    position: absolute;
    top: 266px;
    left: 0;
    width: 100%;
    text-align: center;
    font-weight: 300;
    font-size: 18px;
    color: var(--soft-orange);
  }

  /* Front side */
  .card--front {
    left: 630px;
    background: linear-gradient(135deg, var(--ink-dark) 0%, var(--ink-dark-edge) 100%);
    overflow: hidden;
  }
  .accent-band {
    position: absolute;
    left: 0; top: 0;
    width: 96px; height: 100%;
    background: linear-gradient(180deg, var(--band-warm) 0%, var(--band-deep) 100%);
  }
  .front-mark {
    position: absolute;
    left: 66px; top: 108px;
    width: 60px; height: 60px;
    border-radius: 50%;
    background: var(--mark-amber);
  }
  .front-brand {
    position: absolute;
    left: 158px;
    top: 78px;
  }
  .front-brand__name {
    font-family: "Quicksand", sans-serif;
    font-size: 92px;
    line-height: 1;
    color: var(--brand-orange);
    letter-spacing: 1px;
  }
  .front-brand__tagline {
    font-family: "Lora", serif;
    font-style: italic;
    font-size: 17px;
    color: var(--tagline-grey);
    margin-top: 6px;
    margin-left: 60px;
  }
</style>
</head>
<body>
  <section class="card card--back" aria-label="Card back">
    <div class="back-brand">
      <span class="back-brand__mark"></span>
      <div class="back-brand__text">
        <span class="back-brand__name">Valdor</span>
        <span class="back-brand__tagline">..building what comes next.</span>
      </div>
    </div>
    <div class="contact">
      <p class="contact__email">mara@valdor.holdings</p>
      <p class="contact__role">Client Ambassador</p>
      <p class="contact__line">+61 040 555 120</p>
      <p class="contact__line">Po Box 418 Perth 6000</p>
    </div>
    <div class="back-rule"></div>
    <p class="services">Management. software. construction</p>
  </section>

  <section class="card card--front" aria-label="Card front">
    <div class="accent-band" role="img" aria-label="Decorative colour band along the left edge"></div>
    <span class="front-mark"></span>
    <div class="front-brand">
      <p class="front-brand__name">Valdor</p>
      <p class="front-brand__tagline">..building what comes next.</p>
    </div>
  </section>
</body>
</html>
```